Business Card Design

building company specialistloft conversion,extension ,bathrooms ,kitchens ,painting and decorating all general building work

Industry/Entity Type

Building

Contact Information for Business Card

K&R Home renewal Ltd
tel -07912468305
email-Rmarek07@brickmail.example
web in progres

Font styles to use
Sans Serif

Requirements
Must have
• name of the company
• all contact details
Nice to have
• some of the skills

```html
<!DOCTYPE html>
<html lang="en">
<head>
<meta charset="utf-8">
<title>K&amp;R Home renewal Ltd – Business Cards</title>
<link rel="stylesheet" href="https://fonts.googleapis.com/css2?family=Open+Sans:wght@400;600;800&display=swap">
<style>
  :root {
    --stage: #e9e6e1;
    --card-white: #ffffff;
    --card-grey: #eef0f3;
    --navy: #2d3590;
    --blue: #3b44a8;
    --ink: #1c1c22;
    --icon: #555555;
    --red-light: #ee3b36;
    --red-dark: #c9151d;
    --white: #ffffff;
  }
  * { box-sizing: border-box; margin: 0; padding: 0; }
  html, body {
    width: 1200px; height: 900px; overflow: hidden;
    background: var(--stage);
    font-family: "Open Sans", Arial, sans-serif;
  }
  .stage {
    position: relative; width: 1200px; height: 900px;
    display: flex; align-items: center; justify-content: center; gap: 40px;
  }
  .card {
    position: relative; width: 560px; height: 320px;
    border-radius: 4px; overflow: hidden;
    box-shadow: 0 10px 24px rgba(0,0,0,.18);
  }
  /* Front */
  .card-front {
    background: linear-gradient(160deg, var(--card-white) 40%, var(--card-grey));
  }
  .service-band {
    position: absolute; left: 0; right: 0; bottom: 0; height: 78px;
    background: linear-gradient(90deg, var(--navy), var(--blue));
  }
  .contact-list {
    position: absolute; top: 26px; right: 28px;
    list-style: none; text-align: right;
    font-size: 15px; line-height: 24px; color: var(--ink);
  }
  .contact-list li { display: flex; align-items: center; justify-content: flex-end; gap: 8px; }
  .contact-icon { width: 14px; height: 14px; }
  .brand {
    position: absolute; left: 40px; top: 124px;
    display: flex; align-items: center; gap: 14px;
  }
  .brand-mark { width: 34px; height: 34px; background: var(--navy); flex: none; }
  .brand-name {
    font-weight: 800; font-size: 30px; line-height: 1.05;
    color: var(--navy); text-transform: uppercase;
  }
  .services {
    position: absolute; left: 26px; right: 26px; bottom: 20px;
    font-size: 12.5px; line-height: 18px; color: var(--white);
  }
  /* Back */
  .card-back {
    background: linear-gradient(135deg, var(--red-light), var(--red-dark));
    color: var(--white);
  }
  .back-name {
    position: absolute; left: 0; right: 0; top: 118px; text-align: center;
    font-weight: 800; font-size: 34px; line-height: 1.05; text-transform: uppercase;
  }
  .back-web {
    position: absolute; left: 26px; bottom: 20px;
    font-size: 11px; font-weight: 600; letter-spacing: 1px; text-transform: uppercase;
  }
</style>
</head>
<body>
<main class="stage">
  <section class="card card-front" aria-label="Business card front">
    <div class="service-band" role="img" aria-label="Decorative blue band with coloured stripes"></div>
    <ul class="contact-list">
      <li>07912468305
        <svg class="contact-icon" viewBox="0 0 14 14" aria-hidden="true"><rect x="0.5" y="0.5" width="13" height="13" rx="2" fill="none" stroke="var(--icon)"/><path d="M4,3 l2,0 l0.6,2 l-1,0.8 q0.8,1.8 2.6,2.6 l0.8,-1 l2,0.6 l0,2 q-5,0.5 -7,-7 z" fill="var(--icon)"/></svg>
      </li>
      <li>Rmarek07@brickmail.example
        <svg class="contact-icon" viewBox="0 0 14 14" aria-hidden="true"><rect x="0.5" y="0.5" width="13" height="13" rx="2" fill="none" stroke="var(--icon)"/><rect x="3" y="4" width="8" height="6" fill="none" stroke="var(--icon)"/><path d="M3,4 l4,3 l4,-3" fill="none" stroke="var(--icon)"/></svg>
      </li>
      <li>www.krhomerenewal.example
        <svg class="contact-icon" viewBox="0 0 14 14" aria-hidden="true"><rect x="0.5" y="0.5" width="13" height="13" rx="2" fill="none" stroke="var(--icon)"/><circle cx="7" cy="7" r="4" fill="none" stroke="var(--icon)"/><path d="M3,7 h8 M7,3 v8" stroke="var(--icon)"/></svg>
      </li>
    </ul>
    <div class="brand">
      <span class="brand-mark" aria-hidden="true"></span>
      <h1 class="brand-name">K&amp;R Home<br>renewal Ltd</h1>
    </div>
    <p class="services">Loft conversion | Extension | Bathrooms | Kitchens | Painting and decorating<br>All general building work.</p>
  </section>

  <section class="card card-back" aria-label="Business card back">
    <h2 class="back-name">K&amp;R Home<br>renewal Ltd</h2>
    <p class="back-web">www.krhomerenewal.example</p>
  </section>
</main>
</body>
</html>
```